Donor Thank You Card – Marisol’s Harbor Pregnancy & Family Support

Project Overview:
We are seeking a heartfelt, beautifully designed thank-you card for our nonprofit, Marisol’s Harbor Pregnancy & Family Support. This card will be sent to donors as a tangible expression of gratitude from Marisol’s family.

The design should feel warm, personal, and meaningful—something a recipient would want to keep.

About the Organization
Marisol’s Harbor Pregnancy & Family Support exists to support families navigating complicated pregnancies, prolonged hospital stays, and loss.
The organization was created in honor of Marisol, and everything we do is centered around providing comfort, connection, and a “web of care” during life’s most difficult moments.

Design Objective
Create a thank-you card that conveys:
-Deep gratitude
-Compassion and warmth
-A sense of connection and care
Subtle remembrance and hope
-This should feel personal and heartfelt—not corporate or transactional.

Color Palette: Neutrals (cream, soft beige, warm white)
Soft pastels (blush, sage, muted gold, light blue)
Avoid anything too bold or high contrast

Visual Elements:
Subtle “web” motif (very delicate—not literal or harsh)
Soft sunlight / glow elements (“little sunshine” theme)
Organic textures (linen, paper grain, watercolor feel)
Minimalist line illustrations

Card Format
Standard folded card (5x7 preferred)
Front + inside spread
Front of Card (Minimal + Elegant)

Option 1:
Marisol’s Harbor logo
Short phrase:
“With gratitude”

Option 2:
Logo + subtle design element (sunlight/web texture)
No text or very minimal text

Inside of Card (Main Message)
Include this message:
Because of you, a family will feel supported during one of the most difficult moments of their lives.

Your generosity helps us provide comfort, care, and connection to families navigating complicated pregnancies, prolonged hospital stays, and loss.

From the bottom of our hearts, thank you for being part of this web of support.

With gratitude,
Marisol’s Family

Back of Card:
Logo: (See attachments)
Website URL: www.marisolsharborsupport.org
Small tagline: “Woven with care, held with hope, and touched by a little sunshine.”

Let me know if you need any other variations of the logo.

Thank you!

```html
<!DOCTYPE html>
<html lang="en">
<head>
<meta charset="utf-8">
<title>Marisol’s Harbor – Donor Thank You Card</title>
<link rel="stylesheet" href="https://fonts.googleapis.com/css2?family=Playfair+Display:ital,wght@0,400;0,600;1,400;1,600&family=Great+Vibes&display=swap">
<style>
  :root {
    --stage-dark: #3c3c3c;
    --stage-light: #6f6f6f;
    --sky-pink: #e79ad6;
    --sky-lilac: #b48fdc;
    --sky-blue: #8c88cf;
    --sky-blush: #f2a9d6;
    --frame-gold: #e6c77e;
    --white: #ffffff;
    --script-purple: #8b3fc8;
    --logo-mauve: #9a7ab0;
    --tagline-plum: #7e3f68;
    --url-grey: #555555;
    --inside-lavender: #f3eefa;
    --message-indigo: #3b2396;
    --art-violet: #7a4fd0;
    --art-rose: #d8588a;
  }
  * { box-sizing: border-box; margin: 0; padding: 0; }
  html, body { width: 905px; height: 1200px; overflow: hidden; }
  body {
    position: relative;
    background: radial-gradient(ellipse at 85% 45%, var(--stage-light), var(--stage-dark) 75%);
    font-family: "Playfair Display", Georgia, serif;
  }
  .spread { position: absolute; left: 74px; width: 759px; height: 531px; overflow: hidden; }
  .spread--outside { top: 51px; display: flex; }
  .spread--inside { top: 612px; background: var(--inside-lavender); }

  /* Front cover */
  .card-front {
    position: relative; width: 379px; height: 531px; overflow: hidden;
    background: linear-gradient(170deg, var(--sky-pink) 0%, var(--sky-lilac) 35%, var(--sky-blue) 48%, var(--sky-blush) 70%, var(--sky-lilac) 85%, var(--sky-pink) 100%);
  }
  .front-frame {
    position: absolute; left: 20px; top: 12px; right: 18px; bottom: 13px;
    border: 1px solid var(--frame-gold);
  }
  .front-name, .front-sub, .front-greeting {
    position: absolute; left: 0; width: 100%; text-align: center; white-space: nowrap;
  }
  .front-name {
    top: 228px; color: var(--white); font-size: 36px; font-weight: 400; line-height: 42px;
  }
  .front-sub {
    top: 274px; color: var(--white); font-size: 15px; letter-spacing: 1.5px; line-height: 18px;
  }
  .front-greeting {
    top: 310px; font-family: "Great Vibes", cursive; color: var(--script-purple);
    font-size: 36px; line-height: 44px;
  }

  /* Back cover */
  .card-back { position: relative; width: 380px; height: 531px; background: var(--white); }
  .back-name, .back-sub, .back-tagline, .back-url {
    position: absolute; left: 0; width: 100%; text-align: center; white-space: nowrap;
  }
  .back-name {
    top: 368px; color: var(--logo-mauve); font-size: 24px; line-height: 28px;
  }
  .back-sub {
    top: 396px; color: var(--logo-mauve); font-size: 9.5px; letter-spacing: 1px; line-height: 12px;
  }
  .back-tagline {
    top: 428px; font-style: italic; font-weight: 600; font-size: 7.6px; line-height: 10px;
    color: var(--tagline-plum);
  }
  .back-url {
    top: 489px; font-weight: 600; font-size: 10.5px; line-height: 14px; color: var(--url-grey);
  }

  /* Inside */
  .inside-art {
    position: absolute; left: 27px; top: 106px; width: 410px; height: 410px;
    border-radius: 45% 50% 48% 52%;
    background: radial-gradient(circle at 30% 45%, var(--art-rose) 0%, rgba(216,88,138,0.6) 22%, transparent 42%),
                radial-gradient(circle at 65% 50%, var(--art-violet) 0%, rgba(122,79,208,0.7) 35%, transparent 68%);
    opacity: 0.85;
  }
  .inside-message, .inside-signoff {
    position: absolute; left: 419px; width: 300px;
    text-align: center; font-style: italic; font-size: 12.6px; line-height: 22px;
    color: var(--message-indigo); white-space: nowrap;
  }
  .inside-message { top: 69px; }
  .inside-message p + p { margin-top: 22px; }
  .inside-signoff { top: 357px; }
  .inside-signoff strong { font-weight: 600; }
</style>
</head>
<body>
  <section class="spread spread--outside">
    <article class="card-front">
      <div class="front-frame"></div>
      <div class="front-name">Marisol’s Harbor</div>
      <div class="front-sub">Pregnancy &amp; Family Support</div>
      <div class="front-greeting">With gratitude</div>
    </article>
    <article class="card-back">
      <div class="back-name">Marisol’s Harbor</div>
      <div class="back-sub">Pregnancy &amp; Family Support</div>
      <p class="back-tagline">“Woven with care, held with hope, and touched by a little sunshine.”</p>
      <p class="back-url">www.marisolsharborsupport.org</p>
    </article>
  </section>

  <section class="spread spread--inside">
    <div class="inside-art" role="img" aria-label="Illustration of a pink butterfly beside a cluster of purple and violet flowers"></div>
    <div class="inside-message">
      <p>Because of you, a family will feel supported<br>during one of the most difficult moments of<br>their lives.</p>
      <p>Your generosity helps us provide comfort,<br>care, and connection to families navigating<br>complicated pregnancies, prolonged<br>hospital stays, and loss.</p>
      <p>From the bottom of our hearts, thank you<br>for being part of this web of support.</p>
    </div>
    <div class="inside-signoff">With gratitude,<br><strong>Marisol’s Family</strong></div>
  </section>
</body>
</html>
```